Business card design and logo needed - Photographer

I take photos of weddings, rodeos, snowmobiling.
Need a card to hand out to prospective clients.
Industry/Entity Type
Business
Contact Information for Business Card
Marcus Dolven Photography
Requirements
Must have
- Bold
Black or white base.
My website. www.MarcusDolven.example
Should not have
- camera/ lens/ aperture blades

```html
<!DOCTYPE html>
<html lang="en">
<head>
<meta charset="utf-8">
<title>Marcus Dolven Photography – Business Card</title>
<link rel="stylesheet" href="https://fonts.googleapis.com/css2?family=Quicksand:wght@500&family=Open+Sans:wght@400&display=swap">
<style>
  :root {
    --card-black: #000000;
    --ink-white: #ffffff;
  }
  html, body {
    margin: 0;
    padding: 0;
    width: 1200px;
    height: 693px;
    overflow: hidden;
    background: var(--card-black);
  }
  .card {
    position: relative;
    width: 1200px;
    height: 693px;
    background: var(--card-black);
    color: var(--ink-white);
  }
  .brand {
    position: absolute;
    top: 235px;
    left: 0;
    width: 1200px;
    display: flex;
    justify-content: center;
    align-items: center;
    gap: 30px;
  }
  .brand-mark {
    width: 118px;
    height: 118px;
    background: var(--ink-white);
    flex: none;
  }
  .brand-name {
    font-family: "Quicksand", sans-serif;
    font-weight: 500;
    color: var(--ink-white);
    display: flex;
    flex-direction: column;
    align-items: center;
  }
  .brand-name__person {
    font-size: 66px;
    line-height: 1;
    letter-spacing: 0.5px;
  }
  .brand-name__trade {
    margin-top: 18px;
    font-size: 24px;
    line-height: 1;
    letter-spacing: 13px;
    margin-right: -13px;
  }
  .contact {
    position: absolute;
    top: 604px;
    left: 0;
    width: 1200px;
    display: flex;
    justify-content: center;
    align-items: center;
    font-family: "Open Sans", sans-serif;
    font-weight: 400;
    font-size: 25px;
    letter-spacing: 0.6px;
    color: var(--ink-white);
  }
  .contact__divider {
    margin: 0 30px;
  }
</style>
</head>
<body>
  <main class="card">
    <div class="brand">
      <div class="brand-mark" aria-hidden="true"></div>
      <div class="brand-name">
        <span class="brand-name__person">Marcus Dolven</span>
        <span class="brand-name__trade">PHOTOGRAPHY</span>
      </div>
    </div>
    <p class="contact">
      <span class="contact__web">www.MarcusDolven.example</span>
      <span class="contact__divider">|</span>
      <span class="contact__phone">(555) 014 2290</span>
      <span class="contact__divider">|</span>
      <span class="contact__email">marcusdolven@example.com</span>
    </p>
  </main>
</body>
</html>
```